Used Car Dealer seeks an Amazing Business Card Design

We are looking for a business card design that incorporates our logo and grabs the attention of anyone we give the business card to.

Looking to use the same colors as the logo. Our Logo choice is the black background with Red and Silver/Grey Lettering.

We also would like to see some embossed designs.

Target Market(s)

Used Car Buyers, Automotive, Auto

Industry/Entity Type

Automotive

Contact Information for Business Card

BVEL7K
Gordon Whitlock
482 Tarrow Lane
Suite 207
Brackton, SC 29418
Office (770) 555-0142
Cell (770) 555-0187
bvel7kga@quellmail.com
www.bvel7kga.com

Colors
ffffff
ee3036

Requirements
Must have
• Must include our logo (Black Background with Red and Silver/Grey Lettering)
Nice to have
• Embossed Design. Can be Single or Double Sided.

```html
<!DOCTYPE html>
<html lang="en">
<head>
<meta charset="utf-8">
<title>BVEL7K Business Card</title>
<link rel="stylesheet" href="https://fonts.googleapis.com/css2?family=Lato:wght@400;700&display=swap">
<style>
  :root {
    --page: #ffffff;
    --card: #000000;
    --red: #ee3036;
    --white: #ffffff;
    --silver: #c8c8c8;
  }
  * { margin: 0; padding: 0; box-sizing: border-box; }
  html, body {
    width: 1024px;
    height: 1200px;
    overflow: hidden;
    background: var(--page);
    font-family: "Lato", sans-serif;
  }
  .canvas { position: relative; width: 1024px; height: 1200px; }
  .card {
    position: absolute;
    left: 214px;
    width: 603px;
    height: 372px;
    background: var(--card);
    border-radius: 12px;
    box-shadow: 0 2px 6px rgba(0,0,0,0.35);
    overflow: hidden;
    color: var(--white);
  }
  .card-front { top: 193px; }
  .card-back { top: 631px; }

  .person { position: absolute; left: 43px; top: 40px; }
  .person-name { color: var(--red); font-weight: 700; font-size: 24px; line-height: 28px; }
  .person-role { font-size: 19px; line-height: 24px; }

  .brand {
    position: absolute;
    display: flex;
    align-items: center;
    gap: 10px;
    color: var(--silver);
    font-weight: 700;
  }
  .brand-mark { border-radius: 50%; background: var(--red); }
  .brand-front { left: 350px; top: 62px; font-size: 44px; }
  .brand-front .brand-mark { width: 22px; height: 22px; }
  .brand-back { left: 0; right: 0; top: 150px; justify-content: center; font-size: 62px; }
  .brand-back .brand-mark { width: 30px; height: 30px; }

  .car-band {
    position: absolute;
    left: 0;
    top: 159px;
    width: 603px;
    height: 84px;
    background: linear-gradient(180deg, rgba(238,48,54,0) 0%, rgba(238,48,54,0.55) 55%, rgba(140,20,24,0.35) 100%);
  }

  .contacts { position: absolute; left: 43px; top: 256px; list-style: none; }
  .contacts li {
    display: flex;
    align-items: center;
    height: 22.4px;
    font-size: 17.5px;
  }
  .contacts svg { width: 15px; height: 15px; margin-right: 7px; flex: none; }

  .address {
    position: absolute;
    right: 30px;
    top: 283px;
    text-align: right;
    font-size: 17.5px;
    line-height: 22.4px;
    font-style: normal;
  }
</style>
</head>
<body>
<div class="canvas">
  <section class="card card-front">
    <div class="person">
      <div class="person-name">Gordon Whitlock</div>
      <div class="person-role">Owner</div>
    </div>

    <div class="brand brand-front"><span class="brand-mark"></span>BVEL7K</div>

    <div class="car-band" role="img" aria-label="Red sports car side silhouette sweeping across the card"></div>

    <ul class="contacts">
      <li>
        <svg viewBox="0 0 16 16" fill="var(--red)"><path d="M3.6 1.2l2.2 2.7-1.3 1.6c.9 2 2.6 3.7 4.6 4.6l1.6-1.3 2.7 2.2-1.4 2.2C7.4 13.6 2.4 8.6 1.8 2.6z"/></svg>
        (770) 555-0142
      </li>
      <li>
        <svg viewBox="0 0 16 16" fill="none" stroke="var(--red)" stroke-width="1.6"><rect x="4" y="1" width="8" height="14" rx="1.5"/><line x1="7" y1="12.5" x2="9" y2="12.5"/></svg>
        (770) 555-0187
      </li>
      <li>
        <svg viewBox="0 0 16 16"><rect x="1" y="3" width="14" height="10" fill="var(--red)"/><path d="M1 3l7 6 7-6" fill="none" stroke="#000" stroke-width="1.2"/></svg>
        bvel7kga@quellmail.com
      </li>
      <li>
        <svg viewBox="0 0 16 16" fill="none" stroke="var(--red)" stroke-width="1.3"><circle cx="8" cy="8" r="6.5"/><ellipse cx="8" cy="8" rx="3" ry="6.5"/><line x1="1.5" y1="8" x2="14.5" y2="8"/><line x1="2.5" y1="4.5" x2="13.5" y2="4.5"/><line x1="2.5" y1="11.5" x2="13.5" y2="11.5"/></svg>
        www.bvel7kga.com
      </li>
    </ul>

    <address class="address">
      482 Tarrow Lane<br>
      Suite 207 Brackton<br>
      SC 29418
    </address>
  </section>

  <section class="card card-back">
    <div class="brand brand-back"><span class="brand-mark"></span>BVEL7K</div>
  </section>
</div>
</body>
</html>
```